Legal Stationary

A full set of stationery is required
The image and logo, along with colour, are set and attached.
The style should be modern, clean, and corporate. Not just a basic template off the web.
In addition to the address/website/email/phone fields for DX and KWT number, with the text “the firm is authorised and regulated by the KWT”
All files in all formats will be needed to allow editing after. Initial setup of templates will be required, and details for 4 business cards will be supplied.
Target Market(s)
Consumers of legal services
Industry/Entity Type
Legal

```html
<!DOCTYPE html>
<html lang="en">
<head>
<meta charset="utf-8">
<title>Halden Law Stationery</title>
<link rel="stylesheet" href="https://fonts.googleapis.com/css2?family=Roboto:wght@400;500&display=swap">
<style>
  :root {
    --backdrop: #7b7b7b;
    --paper: #ffffff;
    --brand: #243a91;
    --brand-ink: #1f3488;
    --on-brand: #ffffff;
  }
  * { box-sizing: border-box; margin: 0; padding: 0; }
  html, body { width: 1199px; height: 1200px; overflow: hidden; }
  body {
    background: var(--backdrop);
    font-family: "Roboto", Arial, sans-serif;
    position: relative;
  }
  .sheet { position: absolute; background: var(--paper); }

  /* brand name lockup */
  .brand {
    position: absolute;
    display: flex;
    align-items: center;
    gap: 0.32em;
    font-weight: 500;
    letter-spacing: 0.02em;
    color: var(--brand);
    white-space: nowrap;
  }
  .brand::before {
    content: "";
    width: 0.7em; height: 0.7em;
    background: currentColor;
  }
  .brand--light { color: var(--on-brand); }

  .contact { list-style: none; }
  .contact li {
    display: flex;
    align-items: flex-start;
    gap: 8px;
    line-height: 1.25;
  }
  .contact svg { flex: none; fill: currentColor; margin-top: 0.15em; }

  /* letterhead */
  .letterhead { left: 221px; top: 62px; width: 757px; height: 1072px; }
  .letterhead__stripe { position: absolute; left: 719px; top: 0; }
  .letterhead .brand { left: 66px; top: 50px; font-size: 44px; }
  .letterhead__band { position: absolute; left: 0; top: 972px; }
  .letterhead__contact {
    position: absolute; left: 53px; top: 993px;
    color: var(--on-brand); font-size: 16px;
  }
  .letterhead__contact li + li { margin-top: 6px; }
  .letterhead__address {
    position: absolute; left: 526px; top: 993px;
    color: var(--brand-ink); font-size: 16px;
  }

  /* business cards */
  .card { left: 50px; width: 411px; height: 241px; }
  .card--front { top: 197px; }
  .card--front .brand { left: 112px; top: 40px; font-size: 30px; }
  .card__panel {
    position: absolute; left: 0; top: 138px; width: 206px; height: 85px;
    background: var(--brand); color: var(--on-brand);
    padding: 12px 0 0 36px; font-size: 11.5px;
  }
  .card__panel li + li { margin-top: 4px; }
  .card__name {
    position: absolute; left: 206px; top: 138px; width: 187px; height: 85px;
    border: 1.5px solid var(--brand);
    display: flex; align-items: center; justify-content: center;
    color: var(--brand-ink); font-size: 18px; font-weight: 500;
  }
  .card__name small { font-size: 10px; font-weight: 400; align-self: flex-end; margin-bottom: 33px; }
  .card--back { top: 462px; height: 239px; background: var(--brand); }
  .card--back .brand { left: 50%; top: 104px; transform: translateX(-50%); font-size: 32px; }

  /* envelope */
  .envelope { left: 483px; top: 648px; width: 676px; height: 339px; }
  .envelope .brand { left: 69px; top: 50px; font-size: 32px; }
  .envelope__panel {
    position: absolute; left: 65px; top: 246px; width: 286px; height: 59px;
    background: var(--brand); color: var(--on-brand);
    padding: 10px 0 0 59px; font-size: 13.5px;
  }
  .envelope__panel li + li { margin-top: 3px; }
  .envelope__address {
    position: absolute; left: 351px; top: 246px; width: 259px; height: 59px;
    border: 1.5px solid var(--brand); color: var(--brand-ink);
    padding: 11px 0 0 60px; font-size: 13.5px;
  }
</style>
</head>
<body>

<svg width="0" height="0" style="position:absolute" aria-hidden="true">
  <defs>
    <symbol id="icon-phone" viewBox="0 0 24 24"><path d="M6.6 10.8a15.1 15.1 0 0 0 6.6 6.6l2.2-2.2c.3-.3.7-.4 1-.2 1.1.4 2.3.6 3.6.6.6 0 1 .4 1 1V20c0 .6-.4 1-1 1A17 17 0 0 1 3 4c0-.6.4-1 1-1h3.5c.6 0 1 .4 1 1 0 1.3.2 2.5.6 3.6.1.3 0 .7-.2 1z"/></symbol>
    <symbol id="icon-mail" viewBox="0 0 24 24"><path d="M3 5h18c.6 0 1 .4 1 1v12c0 .6-.4 1-1 1H3c-.6 0-1-.4-1-1V6c0-.6.4-1 1-1zm9 7.5L20.5 7h-17z"/></symbol>
    <symbol id="icon-pin" viewBox="0 0 24 24"><path d="M12 2a7 7 0 0 0-7 7c0 5.2 7 13 7 13s7-7.8 7-13a7 7 0 0 0-7-7zm0 9.5a2.5 2.5 0 1 1 0-5 2.5 2.5 0 0 1 0 5z"/></symbol>
  </defs>
</svg>

<section class="sheet letterhead" aria-label="Letterhead">
  <svg class="letterhead__stripe" width="38" height="590" viewBox="0 0 38 590" aria-hidden="true">
    <polygon points="0,0 38,0 38,590 0,572" fill="var(--brand)"/>
  </svg>
  <div class="brand">HALDEN LAW</div>
  <svg class="letterhead__band" width="365" height="82" viewBox="0 0 365 82" aria-hidden="true">
    <polygon points="0,0 365,0 335,82 0,82" fill="var(--brand)"/>
  </svg>
  <ul class="contact letterhead__contact">
    <li><svg width="12" height="12"><use href="#icon-phone"/></svg>555-0142-7700</li>
    <li><svg width="12" height="12"><use href="#icon-mail"/></svg>hello@haldenlaw.com</li>
  </ul>
  <ul class="contact letterhead__address">
    <li><svg width="12" height="12"><use href="#icon-pin"/></svg>211/A, Address, Street,<br>Pincode-123456</li>
  </ul>
</section>

<section class="sheet card card--front" aria-label="Business card front">
  <div class="brand">HALDEN LAW</div>
  <ul class="contact card__panel">
    <li><svg width="9" height="9"><use href="#icon-phone"/></svg>555-0142-7700</li>
    <li><svg width="9" height="9"><use href="#icon-mail"/></svg>hello@haldenlaw.com</li>
    <li><svg width="9" height="9"><use href="#icon-pin"/></svg>211/A, Address, Street,<br>Pincode-123456</li>
  </ul>
  <div class="card__name">Your Name/<small>CEO</small></div>
</section>

<section class="sheet card card--back" aria-label="Business card back">
  <div class="brand brand--light">HALDEN LAW</div>
</section>

<section class="sheet envelope" aria-label="Envelope">
  <div class="brand">HALDEN LAW</div>
  <ul class="contact envelope__panel">
    <li><svg width="10" height="10"><use href="#icon-phone"/></svg>555-0142-7700</li>
    <li><svg width="10" height="10"><use href="#icon-mail"/></svg>hello@haldenlaw.com</li>
  </ul>
  <ul class="contact envelope__address">
    <li><svg width="10" height="10"><use href="#icon-pin"/></svg>211/A, Address, Street,<br>Pincode-123456</li>
  </ul>
</section>

</body>
</html>
```